Packaging Design for Face Mask Box

We are looking for an attractive but subtle packaging design for Face Masks (for non medical use). 50pcs per box.

The brand name should be "Kelvano". We have not yet got a logo or a text selected (font) for the brand name so we are open to your ideas on how "Kelvano" could look. It could have some elements of fresh air or breathing etc so symbolize clean and healthier air or something along those lines.

The box dimensions should be 180mm (L) x 100mm (W) x 90mm (H).

The box should have a perforation on top - exactly similar to Tissue Box packs. So, in order to access the face masks, the user should tear off the perforation and extract one mask at a time.

As this is not a medical grade face mask, the product should indicate "For Non- Medical Use". Also the heading of the masks should be DISPOSABLE PROTECTIVE FACE MASKS with sub heading 3 PLY FACE MASKS WITH EAR LOOP.

We will also prefer to have the Instructions to use and Precautions which are commonly available on face mask packages. This could be printed either on the sides or on the bottom of the package. There should also be a blank space on one of the sides to print Batch No. Mfg Date and Exp Date.

The box design could have some design resemblance to our company logo which is hereby attached in high resolution. However this is not compulsory.

The following phrases could be mentioned on the box to highlight some of the product features:

Dual Charge Electrostatic fibres for extra filtration
Improved Nose Bridge Strips for better protection
Tri-layer barrier with 3 x 25 g/m2 material
In-house production of filter material for Quality Consistency

I have added 3 samples face mask box designs from other manufacturers for your reference to get an idea of the box shape etc.

If you have any more questions, please feel free to ask.

Good luck!

```html
<!DOCTYPE html>
<html lang="en">
<head>
<meta charset="utf-8">
<title>Kelvano Face Mask Box – Panels</title>
<link href="https://fonts.googleapis.com/css2?family=Orbitron:wght@700;800&family=Exo+2:wght@300;400;500;700;800&display=swap" rel="stylesheet">
<style>
  :root{
    --cyan:#1ec0ec;
    --navy:#0f3f6b;
    --navy-deep:#134a78;
    --sky-1:#cfe9f8;
    --sky-2:#e6f5fd;
    --sky-3:#bfe3f6;
    --blue-mid:#4fb6e6;
    --blue-strong:#1e88d6;
    --mask-1:#8fd0f2;
    --mask-2:#4aaee4;
    --label:#9a9a9a;
    --frame:#9c9c9c;
    --ink:#111;
  }
  *{box-sizing:border-box;margin:0;padding:0}
  html,body{width:1200px;height:965px;overflow:hidden;background:#fff}
  .sheet{position:relative;width:1200px;height:965px;font-family:"Exo 2",sans-serif}
  .panel{position:absolute;overflow:hidden;border:1px solid var(--frame)}
  .panel svg.bg{position:absolute;inset:0;width:100%;height:100%}
  .panel-label{position:absolute;font-family:"Exo 2",sans-serif;font-weight:300;font-size:24px;color:var(--label);letter-spacing:.5px}

  .main-side{left:51px;top:69px;width:652px;height:326px;background:linear-gradient(90deg,var(--sky-3) 0%,var(--sky-2) 45%,#e9f6fd 100%)}
  .side{left:751px;top:72px;width:362px;height:326px;background:#fff}
  .top{left:49px;top:450px;width:431px;height:240px;background:var(--sky-2)}

  .brand{position:absolute;font-family:"Orbitron",sans-serif;font-weight:800;color:var(--cyan);text-align:center;letter-spacing:1px;line-height:1}
  .heading{position:absolute;font-family:"Exo 2",sans-serif;font-weight:800;color:var(--navy);text-align:center;line-height:1;letter-spacing:.3px}
  .pill{position:absolute;background:var(--navy-deep);color:#fff;border-radius:10px;text-align:center;font-weight:400;white-space:nowrap}

  .feature{position:absolute;display:flex;align-items:center;gap:6px}
  .feature-icon{width:34px;height:34px;flex:none}
  .feature-text{font-size:10px;line-height:12.5px;color:var(--navy);letter-spacing:.5px;font-weight:400}

  .count{position:absolute;color:var(--navy);text-align:center;line-height:1}
  .count-num{font-weight:800}
  .count-unit{font-weight:700}
  .count-note{display:block;font-weight:700}

  .mask-art{position:absolute}
  .company{position:absolute;display:flex;align-items:center;gap:5px;color:var(--navy);font-weight:500;letter-spacing:.4px;white-space:nowrap}
  .company-mark{background:var(--navy-deep);flex:none}

  .print-field{position:absolute;color:var(--ink);line-height:1.15}
  .print-field .field-name{font-size:9px;display:block}
  .print-field .field-value{font-size:12px;display:block;letter-spacing:.3px}
</style>
</head>
<body>
<div class="sheet">

  <!-- Main side -->
  <section class="panel main-side">
    <svg class="bg" viewBox="0 0 652 326" aria-hidden="true">
      <defs>
        <radialGradient id="glow" cx="0.5" cy="0.5" r="0.5">
          <stop offset="0" stop-color="#fff" stop-opacity="1"/>
          <stop offset="1" stop-color="#fff" stop-opacity="0"/>
        </radialGradient>
        <linearGradient id="lightArc" x1="0" y1="0" x2="1" y2="0">
          <stop offset="0" stop-color="#bfe6f8"/>
          <stop offset="1" stop-color="#d7f0fb"/>
        </linearGradient>
      </defs>
      <circle cx="520" cy="90" r="70" fill="url(#glow)" opacity=".8"/>
      <circle cx="610" cy="470" r="230" fill="url(#lightArc)"/>
      <circle cx="395" cy="400" r="120" fill="var(--blue-mid)"/>
      <circle cx="510" cy="430" r="150" fill="#8fd0f2" opacity=".55"/>
      <path d="M446 326 A150 150 0 0 1 540 300 L540 326 Z" fill="var(--blue-strong)"/>
    </svg>

    <div class="mask-art" role="img" aria-label="Photo of a blue 3-ply face mask with white ear loops"
         style="left:378px;top:55px;width:272px;height:178px;border-radius:40% 30% 45% 50%;background:linear-gradient(160deg,var(--mask-1),var(--mask-2));"></div>

    <div class="brand" style="left:60px;top:60px;width:300px;font-size:48px;">KELVANO</div>
    <div class="heading" style="left:50px;top:122px;width:320px;font-size:20px;">DISPOSABLE PROTECTIVE<br>FACE MASKS</div>
    <div class="pill" style="left:102px;top:168px;width:213px;height:19px;font-size:12px;line-height:19px;">3 Ply Face Masks with Ear Loop</div>

    <div class="feature" style="left:36px;top:213px;">
      <svg class="feature-icon" viewBox="0 0 34 34" aria-hidden="true"><circle cx="17" cy="17" r="17" fill="var(--navy-deep)"/><rect x="8" y="12" width="18" height="10" rx="4" fill="none" stroke="#fff" stroke-width="1.3"/><path d="M10 16h14M10 19h14" stroke="#fff" stroke-width="1"/></svg>
      <span class="feature-text">Dual Charge Electrostatic<br>fibres for extra filtration</span>
    </div>
    <div class="feature" style="left:36px;top:256px;">
      <svg class="feature-icon" viewBox="0 0 34 34" aria-hidden="true"><circle cx="17" cy="17" r="17" fill="var(--navy-deep)"/><path d="M14 8v8l-4 6h14l-4-6V8" fill="none" stroke="#fff" stroke-width="1.3"/><circle cx="14" cy="24" r="2" fill="none" stroke="#fff"/><circle cx="20" cy="24" r="2" fill="none" stroke="#fff"/></svg>
      <span class="feature-text">Improved Nose Bridge Strips<br>for better protection</span>
    </div>
    <div class="feature" style="left:230px;top:213px;">
      <svg class="feature-icon" viewBox="0 0 34 34" aria-hidden="true"><circle cx="17" cy="17" r="17" fill="var(--navy-deep)"/><path d="M17 7l8 3v6c0 5-4 9-8 11-4-2-8-6-8-11v-6z" fill="none" stroke="#fff" stroke-width="1.3"/><path d="M17 10l5 2v4c0 3-2 6-5 7-3-1-5-4-5-7v-4z" fill="none" stroke="#fff" stroke-width="1"/></svg>
      <span class="feature-text">Tri-layer barrier with<br>3 x 25 g/m2 material</span>
    </div>
    <div class="feature" style="left:230px;top:257px;">
      <svg class="feature-icon" viewBox="0 0 34 34" aria-hidden="true"><circle cx="17" cy="17" r="17" fill="var(--navy-deep)"/><path d="M7 17l10 6 10-6M7 20l10 6 10-6M7 14l10-6 10 6-10 6z" fill="none" stroke="#fff" stroke-width="1.2"/></svg>
      <span class="feature-text">In-house production of filter<br>material for Quality Consistency</span>
    </div>

    <div class="count" style="left:488px;top:250px;width:130px;">
      <span class="count-num" style="font-size:30px;">50</span><span class="count-unit" style="font-size:13px;"> pcs</span>
      <span class="count-note" style="font-size:12px;margin-top:2px;">For Non-Medical Use</span>
    </div>
  </section>
  <div class="panel-label" style="left:47px;top:409px;">MAIN SIDE</div>

  <!-- Side -->
  <section class="panel side">
    <svg class="bg" viewBox="0 0 362 326" aria-hidden="true">
      <circle cx="-20" cy="330" r="90" fill="var(--sky-2)"/>
    </svg>
    <div class="company" style="left:100px;top:80px;font-size:11px;">
      <span class="company-mark" style="width:9px;height:9px;"></span>NORVALE TRADING FZC
    </div>
    <div class="mask-art" role="img" aria-label="Photo of a blue 3-ply face mask, front view with ear loops"
         style="left:84px;top:113px;width:197px;height:107px;border-radius:30% 30% 50% 50%;background:linear-gradient(180deg,var(--mask-1),var(--mask-2));"></div>
    <div class="print-field" style="left:35px;top:239px;"><span class="field-name">Expire Date:</span><span class="field-value">00.00.0000</span></div>
    <div class="print-field" style="left:35px;top:269px;"><span class="field-name">Manufacture Date:</span><span class="field-value">00.00.0000</span></div>
    <div class="print-field" style="left:136px;top:269px;"><span class="field-name">Batch No:</span><span class="field-value">00.00.0000</span></div>
  </section>
  <div class="panel-label" style="left:752px;top:409px;">SIDE</div>

  <!-- Top -->
  <section class="panel top">
    <svg class="bg" viewBox="0 0 431 240" aria-hidden="true">
      <circle cx="440" cy="300" r="135" fill="#aadcf4"/>
      <circle cx="250" cy="310" r="80" fill="var(--blue-mid)"/>
      <path d="M287 240 A80 80 0 0 1 330 205 A135 135 0 0 1 345 240 Z" fill="var(--blue-strong)"/>
      <path d="M86 49 H344 Q359 49 359 64 V131 Q359 146 340 150 L260 173 Q240 178 230 190 Q215 205 200 190 Q190 178 170 173 L90 150 Q71 146 71 131 V64 Q71 49 86 49 Z"
            fill="none" stroke="var(--navy)" stroke-width="0.9" stroke-dasharray="4 3"/>
    </svg>
    <div class="brand" style="left:65px;top:68px;width:300px;font-size:30px;">KELVANO</div>
    <div class="heading" style="left:65px;top:112px;width:300px;font-size:13px;">DISPOSABLE PROTECTIVE<br>FACE MASKS</div>
    <div class="pill" style="left:145px;top:142px;width:141px;height:12px;font-size:8px;line-height:12px;border-radius:6px;">3 Ply Face Masks with Ear Loop</div>
    <div class="company" style="left:24px;top:203px;font-size:7.5px;">
      <span class="company-mark" style="width:7px;height:7px;"></span>NORVALE TRADING FZC
    </div>
    <div class="count" style="left:330px;top:188px;width:85px;">
      <span class="count-num" style="font-size:20px;">50</span><span class="count-unit" style="font-size:9px;"> pcs</span>
      <span class="count-note" style="font-size:8px;">For Non-Medical Use</span>
    </div>
  </section>
  <div class="panel-label" style="left:47px;top:703px;">TOP</div>

</div>
</body>
</html>
```